Lawn Maintenance Company needs attractive add for local newspaper

My company Fennick Yard Service offers many lawn and yard services but I want this add to focus on one specific service we offer.
- Lawn Fertilizer and Weed Control -

This will be an add for our local newspaper, likely a 1/4 page

Some more information about this service.
Our customers generally call us when their lawn is over run with weeds or is performing poorly. Most of the time we set them up with a program and we return to their property every 4 - 5 weeks for another application. 95% of our customers return the following year for the same program. If the customer wishes we will also do a one time application

email: fennickyardservice@example.net
phone: call or text 555-418-7390

Target Market(s)

- Local small towns, populations less than 20,000
- Residential and Commercial customers with lawns
- People who are using the competitors service and aren't happy with it

Industry/Entity Type

Lawn Care

Requirements
Must have
• Must include our logo, email address and phone number
• - Logo
• - Email address and phone number (call or text)
• - Must focus on the service we want to sell (fertilizer and weed control)
Nice to have
• Some phrases or words that should be included, does not need to be word for word as long as the point is made
• - We service both Residential & Commercial properties
• - We offer professional service that can dramatically improve your lawn whether you are looking for a single application or a season long fertilizer/weed control program
• - Our lawn techs are licensed and certified applicators
Should not have
• I do not want any stock pictures of people, houses or equipment.

```html
<!DOCTYPE html>
<html lang="en">
<head>
<meta charset="utf-8">
<title>Fennick Yard Service – Fertilizer &amp; Weed Control</title>
<link rel="stylesheet" href="https://fonts.googleapis.com/css2?family=Libre+Baskerville:ital,wght@0,400;0,700;1,400&display=swap">
<style>
  :root {
    --sky-top: #8fc3e8;
    --sky-low: #cfe6f3;
    --foliage: #4f8f3a;
    --lawn: #5fae2e;
    --lawn-deep: #3f7d22;
    --brand-green: #3e9a2c;
    --brand-dark: #1f3d1a;
    --banner-orange: #e0571f;
    --cert-blue: #2d4a9c;
    --white: #ffffff;
    --ink: #1e1e1e;
    --page: #f2f2f2;
  }
  * { box-sizing: border-box; margin: 0; padding: 0; }
  html, body { width: 1200px; height: 1018px; overflow: hidden; background: var(--page); }
  body { font-family: "Libre Baskerville", Georgia, serif; }

  .ad {
    position: relative;
    width: 1200px;
    height: 1018px;
    overflow: hidden;
  }
  .ad-photo {
    position: absolute;
    inset: 0;
    background:
      linear-gradient(180deg, var(--sky-top) 0%, var(--sky-low) 38%, var(--foliage) 52%, var(--lawn) 70%, var(--lawn-deep) 100%);
  }

  .brand {
    position: absolute;
    top: 110px;
    left: 0;
    right: 0;
    display: flex;
    align-items: center;
    justify-content: center;
    gap: 24px;
  }
  .brand-dot {
    width: 70px;
    height: 70px;
    border-radius: 50%;
    background: var(--brand-green);
  }
  .brand-name {
    font-weight: 700;
    font-size: 64px;
    color: var(--brand-dark);
    letter-spacing: 1px;
  }

  .offer-banner {
    position: absolute;
    top: 270px;
    left: 110px;
    width: 980px;
    padding: 26px 50px;
    background: var(--banner-orange);
    border-radius: 70px;
    color: var(--white);
    text-align: center;
  }
  .offer-banner p { font-size: 30px; line-height: 1.35; }
  .offer-banner strong { font-size: 40px; font-weight: 700; display: block; }

  .cert-box {
    position: absolute;
    top: 470px;
    right: 60px;
    width: 440px;
    padding: 28px 30px;
    background: var(--cert-blue);
    color: var(--white);
    font-style: italic;
    font-size: 30px;
    line-height: 1.4;
    text-align: center;
  }

  .contact-block {
    position: absolute;
    left: 230px;
    bottom: 0;
    width: 130px;
    height: 150px;
    background: var(--banner-orange);
  }
  .contact-bar {
    position: absolute;
    left: 360px;
    bottom: 20px;
    width: 840px;
    height: 170px;
    padding: 24px 40px;
    background: var(--white);
    color: var(--ink);
    display: flex;
    flex-direction: column;
    justify-content: center;
    gap: 14px;
  }
  .contact-line { display: flex; align-items: center; gap: 18px; font-size: 34px; }
  .contact-line svg { flex: none; }
  .contact-phone { font-size: 34px; }
  .contact-phone b { font-size: 50px; font-weight: 400; }
</style>
</head>
<body>
  <section class="ad">
    <div class="ad-photo" role="img" aria-label="Photo of a lush green lawn and flowering garden beneath a blue sky with trees"></div>

    <div class="brand">
      <span class="brand-dot"></span>
      <span class="brand-name">Fennick Yard Service</span>
    </div>

    <div class="offer-banner">
      <p>We offer single applications or season long</p>
      <p><strong>Fertilizer &amp; Weed control programs</strong></p>
    </div>

    <div class="cert-box">All of our technicians<br>are certified by<br>Prairie Environment Board</div>

    <div class="contact-block"></div>
    <div class="contact-bar">
      <div class="contact-line">
        <svg width="40" height="30" viewBox="0 0 40 30" aria-hidden="true">
          <rect x="1" y="1" width="38" height="28" fill="var(--ink)"/>
          <path d="M1 1 L20 17 L39 1" fill="none" stroke="var(--white)" stroke-width="3"/>
        </svg>
        <span>fennickyardservice@example.net</span>
      </div>
      <div class="contact-phone">Call or Text: <b>555-418-7390</b></div>
    </div>
  </section>
</body>
</html>
```